Trevally's Flyer Design

Trevally Pty Ltd provides professional application support for various Australian Visas. Please refer to business card on file for details. This flyer should attract attention from overseas students currently studying in colleges and universities in Melbourne wishing to update, renew or extend their current visas. In Australia when an overseas student changes course from the original course whether because it is too hard (fail) or not suitable etc... they will need to apply for a new visa after being approved by another college for a new course. Trevally offers a fast, reliable, professional service provided by 'KELT Registered Migration Agent' and migration lawyer. We would like to see attention grapping using striking VISA word, student graduate hat, etc....We will hand these out to students at colleges, display at counters at student accommodation apartment lobby etc...Color wise, we are not fuss but typical Australian colours are green, yellow, white and blue.

```html
<!DOCTYPE html>
<html lang="en">
<head>
<meta charset="utf-8">
<title>Trevally Visa Services Flyer</title>
<link href="https://fonts.googleapis.com/css2?family=Raleway:ital,wght@0,400;0,500;0,700;0,800;1,400&family=Montserrat:wght@500;700&display=swap" rel="stylesheet">
<style>
  :root {
    --page-bg: #dfe6ea;
    --paper: #ffffff;
    --ink: #2b2b2b;
    --brand-green: #2e8b57;
    --teal: #4ea592;
    --teal-dark: #3f9a86;
    --blue: #4a68bf;
    --yellow: #d6dd3a;
    --leaf: #2f8f55;
    --brand-blue: #2f49a6;
    --divider: rgba(255,255,255,0.75);
    --photo-top: #8fb2cc;
    --photo-mid: #5f7fa6;
    --photo-low: #3d5a86;
  }
  * { box-sizing: border-box; margin: 0; padding: 0; }
  html, body { width: 1154px; height: 1200px; overflow: hidden; }
  body {
    background: var(--page-bg);
    font-family: "Raleway", Arial, sans-serif;
    color: var(--ink);
  }
  .flyer {
    position: absolute;
    left: 174px; top: 30px;
    width: 806px; height: 1140px;
    background: var(--paper);
    overflow: hidden;
    box-shadow: 0 6px 24px rgba(0,0,0,0.18);
  }
  /* Header */
  .header { position: absolute; left: 0; top: 0; width: 100%; height: 222px; }
  .header__question {
    position: absolute; left: 44px; top: 58px; width: 540px;
    font-size: 29px; font-weight: 500; line-height: 1.15; letter-spacing: 0.5px;
    text-transform: uppercase; color: #333;
    padding-bottom: 12px; border-bottom: 2px solid var(--brand-green);
  }
  .header__answer {
    position: absolute; left: 44px; top: 146px;
    font-size: 33px; font-weight: 800; line-height: 1.05; letter-spacing: 0.8px;
    text-transform: uppercase; color: var(--brand-green);
  }
  .brand {
    position: absolute; right: 44px; top: 50px; width: 160px;
    text-align: center;
  }
  .brand__mark {
    display: block; width: 104px; height: 104px; margin: 0 auto 12px;
    border-radius: 50%; border: 5px solid var(--brand-green);
  }
  .brand__name { font-size: 30px; font-weight: 500; color: var(--brand-blue); }

  /* Middle band */
  .band { position: absolute; left: 0; top: 222px; width: 100%; height: 660px; }
  .stripes { position: absolute; left: 0; top: 0; width: 460px; height: 100%; }
  .stripe { position: absolute; left: 0; width: 100%; }
  .stripe--teal { top: 0; height: 352px; background: var(--teal-dark); }
  .stripe--blue { top: 352px; height: 94px; background: var(--blue); }
  .stripe--yellow { top: 446px; height: 100px; background: var(--yellow); }
  .stripe--green { top: 546px; height: 114px; background: var(--leaf); }
  .band__photo {
    position: absolute; left: 40px; top: 22px; width: 380px; height: 626px;
    border-radius: 6px;
    background: linear-gradient(180deg, var(--photo-top) 0%, var(--photo-mid) 45%, var(--photo-low) 100%);
    opacity: 0.9;
  }
  .services { position: absolute; left: 460px; top: 0; width: 346px; height: 100%; }
  .service-group { color: #fff; font-family: "Montserrat", Arial, sans-serif; font-size: 19px; }
  .service-group--primary { background: var(--teal); height: 300px; padding: 26px 30px 0 24px; }
  .service-group--primary .service {
    padding: 16px 0 20px; border-bottom: 2px dashed var(--divider);
  }
  .service-group--primary .service:last-child { border-bottom: none; }
  .service-group--blue { background: var(--blue); height: 118px; padding: 28px 24px; }
  .service-group--yellow { background: var(--yellow); height: 118px; padding: 28px 24px; color: #222; }
  .service-group--teal { background: var(--teal); height: 124px; padding: 30px 24px; }
  .service { font-weight: 500; line-height: 1.35; }
  .service b { font-weight: 700; }

  /* Footer */
  .audience {
    position: absolute; left: 44px; top: 920px; width: 320px;
    font-size: 19px; line-height: 1.3;
  }
  .audience__cta {
    position: absolute; left: 44px; top: 1030px; width: 350px; height: 110px;
    background: var(--leaf); color: #fff;
    font-size: 24px; font-weight: 500; line-height: 1.1; text-transform: uppercase;
    padding: 18px 16px;
  }
  .contact { position: absolute; left: 470px; top: 908px; width: 310px; list-style: none; }
  .contact li {
    display: flex; align-items: center; gap: 12px;
    font-size: 16px; line-height: 1.3; margin-bottom: 12px;
  }
  .contact li.contact__phone { font-size: 20px; }
  .contact svg { flex: none; width: 20px; height: 20px; fill: var(--brand-blue); }
  .note {
    position: absolute; left: 470px; top: 1068px; width: 320px;
    font-size: 15px; font-style: italic; line-height: 1.35;
  }
</style>
</head>
<body>
<main class="flyer">
  <header class="header">
    <h2 class="header__question">Wishing to update, renew or extend your current visas</h2>
    <h1 class="header__answer">We got you covered<br>from all your visa needs</h1>
    <div class="brand">
      <span class="brand__mark"></span>
      <span class="brand__name">Trevally</span>
    </div>
  </header>

  <section class="band">
    <div class="stripes">
      <div class="stripe stripe--teal"></div>
      <div class="stripe stripe--blue"></div>
      <div class="stripe stripe--yellow"></div>
      <div class="stripe stripe--green"></div>
      <div class="band__photo" role="img" aria-label="Photo: three smiling overseas students standing together holding laptops, notebooks and folders"></div>
    </div>
    <div class="services">
      <div class="service-group service-group--primary">
        <p class="service">Student Visa | <b>Visa Du Hoc</b></p>
        <p class="service">Working Visa | <b>Visa Lam Viec</b></p>
        <p class="service">Bridging Visa | <b>Visa Tam Tru</b></p>
      </div>
      <div class="service-group service-group--blue">
        <p class="service">Permanent Residency Visa |<br><b>Visa Thuong Tru</b></p>
      </div>
      <div class="service-group service-group--yellow">
        <p class="service">Extension of Visa Transfer |<br><b>Gia Han Visa/Chuyen</b></p>
      </div>
      <div class="service-group service-group--teal">
        <p class="service"><b>Employer<br>Sponshorship Visa</b></p>
      </div>
    </div>
  </section>

  <p class="audience">Our Services are for overseas students currently studying in colleges and universities in Melbourne wishing to</p>
  <p class="audience__cta">Update, renew or extend their current visas.</p>

  <ul class="contact">
    <li><svg viewBox="0 0 24 24" aria-hidden="true"><path d="M12 2a7 7 0 0 0-7 7c0 5 7 13 7 13s7-8 7-13a7 7 0 0 0-7-7zm0 9.5A2.5 2.5 0 1 1 12 6.5a2.5 2.5 0 0 1 0 5z"/></svg><span>Suite 4 Level 7, 218 Wattle Lane<br>Melbourne, Victoria 3000 Australia</span></li>
    <li class="contact__phone"><svg viewBox="0 0 24 24" aria-hidden="true"><path d="M7 1h10a2 2 0 0 1 2 2v18a2 2 0 0 1-2 2H7a2 2 0 0 1-2-2V3a2 2 0 0 1 2-2zm0 3v14h10V4zm5 15.5a1 1 0 1 0 0 2 1 1 0 0 0 0-2z"/></svg><span>+61 3 5550 2846</span></li>
    <li><svg viewBox="0 0 24 24" aria-hidden="true"><path d="M2 5h20v14H2zm2 2v.5l8 5.5 8-5.5V7zm0 3v7h16v-7l-8 5.5z"/></svg><span>admin@trevally.net.au</span></li>
    <li><svg viewBox="0 0 24 24" aria-hidden="true"><path d="M12 2a10 10 0 1 0 0 20 10 10 0 0 0 0-20zm6.9 9h-3a15 15 0 0 0-1.3-6A8 8 0 0 1 18.9 11zM12 4.1c1 1.4 1.8 4 1.9 6.9h-3.8c.1-2.9.9-5.5 1.9-6.9zM9.4 5a15 15 0 0 0-1.3 6h-3A8 8 0 0 1 9.4 5zm-4.3 8h3a15 15 0 0 0 1.3 6 8 8 0 0 1-4.3-6zm6.9 6.9c-1-1.4-1.8-4-1.9-6.9h3.8c-.1 2.9-.9 5.5-1.9 6.9zm2.6-.9a15 15 0 0 0 1.3-6h3a8 8 0 0 1-4.3 6z"/></svg><span>www.trevally.net.au</span></li>
  </ul>
  <p class="note">Trevally offers a fast, reliable, professional service provided by 'KELT Registered Migration Agent' and migration lawyer.</p>
</main>
</body>
</html>
```